Label Design for Nuts package*

Develop the design for a label for nuts sold in a paperbag.

you can find our website here: www.kornfeld-snack.de.
Here comes the link to our catalogue: https://www.blattwerk-docs.com/de/document/read/48172956/kornfeld-premium-snacks-gesamtkatalog-2019

With this product we are targeting private customers who want to buy nuts with plastic free packaging online.
The colours of the label should fit the brown paper bag.

```html
<!DOCTYPE html>
<html lang="de">
<head>
<meta charset="utf-8">
<title>Kornfeld Cashewkerne – Etikett</title>
<link href="https://fonts.googleapis.com/css2?family=Josefin+Sans:wght@300&family=Roboto+Slab:wght@400&family=Archivo+Black&display=swap" rel="stylesheet">
<style>
  :root {
    --page: #ffffff;
    --kraft: #ae9470;
    --kraft-line: #a58a65;
    --panel: #b0956c;
    --frame: #5a2e1a;
    --nut-light: #e2c09a;
    --nut: #d2a579;
    --nut-dark: #a87850;
    --white: #ffffff;
    --gold-1: #b89a56;
    --gold-2: #f4e3a4;
    --gold-3: #9c8146;
  }
  * { margin: 0; padding: 0; box-sizing: border-box; }
  html, body { width: 1200px; height: 1000px; overflow: hidden; background: var(--page); }
  .canvas { position: relative; width: 1200px; height: 1000px; }
  .label {
    position: absolute; left: 284px; top: 120px; width: 632px; height: 760px;
    background: repeating-linear-gradient(90deg, var(--kraft) 0 4px, var(--kraft-line) 4px 5px);
  }
  .artwork { position: absolute; left: 0; top: 0; width: 1200px; height: 1000px; }
  .brand-mark {
    position: absolute; left: 568px; top: 230px; width: 64px; height: 64px;
    border-radius: 50%; background: var(--white);
  }
  .brand {
    position: absolute; left: 0; width: 1200px; top: 316px; text-align: center;
    font-family: "Josefin Sans", sans-serif; font-weight: 300;
    font-size: 62px; letter-spacing: 24px; text-indent: 24px;
    color: var(--white); line-height: 1;
  }
  .tagline {
    position: absolute; left: 0; width: 1200px; top: 390px; text-align: center;
    font-family: "Roboto Slab", serif; font-weight: 400; font-size: 19px;
    letter-spacing: 4px; text-indent: 4px; color: var(--white); line-height: 1;
  }
  .product {
    position: absolute; left: 0; width: 1200px; top: 474px; text-align: center;
    font-family: "Archivo Black", sans-serif; font-weight: 400; font-size: 48px; line-height: 1;
    background: linear-gradient(90deg, var(--gold-1), var(--gold-2) 50%, var(--gold-3));
    -webkit-background-clip: text; background-clip: text; color: transparent;
  }
  .product-rule {
    position: absolute; left: 386px; top: 534px; width: 430px; height: 11px;
    background: linear-gradient(90deg, var(--gold-1), var(--gold-2) 50%, var(--gold-3));
  }
</style>
</head>
<body>
<main class="canvas">
  <div class="label"></div>

  <svg class="artwork" viewBox="0 0 1200 1000" xmlns="http://www.w3.org/2000/svg">
    <defs>
      <linearGradient id="nut-tone" x1="0" y1="0" x2="0.3" y2="1">
        <stop offset="0" stop-color="var(--nut-light)"/>
        <stop offset="0.55" stop-color="var(--nut)"/>
        <stop offset="1" stop-color="var(--nut-dark)"/>
      </linearGradient>
      <linearGradient id="cashew-tone" x1="0" y1="0" x2="1" y2="1">
        <stop offset="0" stop-color="#f2e8d2"/>
        <stop offset="0.7" stop-color="#e4d5b2"/>
        <stop offset="1" stop-color="#6aa63f"/>
      </linearGradient>
    </defs>

    <g class="nut-border" fill="url(#nut-tone)">
      <path role="img" aria-label="Gehackte Nüsse und ein Blatt entlang der Oberkante"
        d="M314,212 C310,190 322,168 345,158 C380,146 420,150 460,156 C520,150 580,146 640,148
           C700,146 760,150 820,156 C850,156 872,170 880,190 C890,210 890,228 880,238
           L862,226 C840,206 820,196 805,183 C720,190 660,168 600,170 C540,168 480,190 395,183
           C380,196 360,206 335,214 Z"/>
      <path role="img" aria-label="Gehackte Nüsse unten links"
        d="M320,740 C340,732 336,760 336,790 C360,794 380,804 395,817 C430,812 470,814 500,820
           C496,834 470,842 440,838 C400,842 360,840 335,834 C314,826 310,790 314,760 Z"/>
      <path role="img" aria-label="Gehackte Nüsse unten rechts"
        d="M866,734 C884,740 890,770 886,796 C882,822 864,836 830,838 C790,842 740,840 700,838
           C684,836 680,826 690,820 C730,814 770,812 805,817 C820,804 840,794 864,790 Z"/>
    </g>

    <g class="frame">
      <path fill="var(--panel)" stroke="var(--frame)" stroke-width="4"
        d="M335,200 C360,206 380,196 395,183 C480,190 540,168 600,170 C660,168 720,190 805,183 C820,196 840,206 865,200
           L865,800 C840,794 820,804 805,817 C720,810 660,832 600,830 C540,832 480,810 395,817 C380,804 360,794 335,800 Z"/>
      <path fill="none" stroke="var(--frame)" stroke-width="1.5"
        d="M347,210 C368,214 386,206 400,195 C482,201 542,180 600,182 C658,180 718,201 800,195 C814,206 832,214 853,210
           L853,790 C832,786 814,794 800,805 C718,799 658,820 600,818 C542,820 482,799 400,805 C386,794 368,786 347,790 Z"/>
    </g>

    <g class="tagline-rule" stroke="var(--white)" fill="none">
      <line x1="478" y1="421" x2="722" y2="421" stroke-width="1"/>
      <circle cx="599" cy="421" r="4" stroke-width="2"/>
    </g>

    <ellipse role="img" aria-label="Cashewkerne mit grünen Blättern" cx="582" cy="800" rx="100" ry="54" fill="url(#cashew-tone)"/>
  </svg>

  <div class="brand-mark"></div>
  <div class="brand">kornfeld</div>
  <div class="tagline">PREMIUM SNACKS</div>
  <h1 class="product">CASHEWKERNE</h1>
  <div class="product-rule"></div>
</main>
</body>
</html>
```